Medical Company in need of Modern business card design for new Wound Care clinic.

Modern business card design for our Woundcare company. Logo and description of services can be found on our website; https://www.tovrel-woundcare.com/

```html
<!DOCTYPE html>
<html lang="en">
<head>
<meta charset="utf-8">
<title>Tovrel Woundcare – Business Card</title>
<link href="https://fonts.googleapis.com/css2?family=Arimo:wght@400;700&family=Montserrat:wght@400&display=swap" rel="stylesheet">
<style>
  :root {
    --backdrop: #e6e5e3;
    --card: #2b2b2c;
    --card-deep: #222223;
    --gold: #c8912e;
    --gold-light: #e0b04a;
    --ink-light: #eeeeee;
    --rule: #9a9a9a;
  }
  * { box-sizing: border-box; margin: 0; padding: 0; }
  html, body { width: 1200px; height: 801px; overflow: hidden; }
  body {
    background: var(--backdrop);
    position: relative;
    font-family: "Arimo", Arial, sans-serif;
  }
  .card {
    position: absolute;
    top: 246px;
    width: 540px;
    height: 309px;
    background: var(--card);
    border: 2px solid var(--gold);
    overflow: hidden;
  }
  .card--front { left: 40px; }
  .card--back { left: 620px; }

  .brand {
    position: absolute;
    left: 44px;
    top: 74px;
    display: flex;
    align-items: center;
    gap: 14px;
  }
  .brand__mark {
    width: 22px;
    height: 22px;
    background: var(--gold);
  }
  .brand__name {
    font-family: "Montserrat", Arial, sans-serif;
    font-weight: 400;
    font-size: 21px;
    letter-spacing: 6px;
    color: var(--gold);
    white-space: nowrap;
  }

  .person {
    position: absolute;
    left: 44px;
    top: 150px;
    width: 190px;
  }
  .person__name {
    font-weight: 700;
    font-size: 19px;
    color: var(--gold);
    letter-spacing: 0.3px;
  }
  .person__role {
    font-size: 14px;
    color: var(--ink-light);
    margin-top: 4px;
    text-align: right;
  }

  .divider {
    position: absolute;
    left: 250px;
    top: 140px;
    width: 1px;
    height: 64px;
    background: var(--rule);
  }

  .contacts {
    position: absolute;
    left: 266px;
    top: 138px;
    list-style: none;
  }
  .contacts li {
    display: flex;
    align-items: center;
    gap: 8px;
    font-size: 13.5px;
    color: var(--ink-light);
    line-height: 22px;
  }
  .contacts svg { width: 12px; height: 12px; flex: none; }

  .address {
    position: absolute;
    left: 44px;
    bottom: 30px;
    font-size: 14px;
    color: var(--ink-light);
    white-space: nowrap;
  }

  .pattern {
    position: absolute;
    inset: 0;
    background: radial-gradient(ellipse at 70% 40%, #3a3a3b 0%, var(--card) 55%, var(--card-deep) 100%);
  }
  .back-name {
    position: absolute;
    left: 300px;
    top: 170px;
    font-family: "Arimo", Arial, sans-serif;
    font-weight: 700;
    font-size: 24px;
    letter-spacing: 3px;
    color: var(--gold-light);
  }
</style>
</head>
<body>

<section class="card card--front" aria-label="Business card front">
  <div class="brand">
    <span class="brand__mark"></span>
    <span class="brand__name">TOVREL WOUNDCARE</span>
  </div>

  <div class="person">
    <p class="person__name">MARCUS DELANE</p>
    <p class="person__role">Manager</p>
  </div>

  <span class="divider"></span>

  <ul class="contacts">
    <li>
      <svg viewBox="0 0 12 12" aria-hidden="true"><path d="M2.5 1h2l1 2.6-1.3 1a6 6 0 0 0 3.2 3.2l1-1.3 2.6 1v2a1 1 0 0 1-1 1A9.5 9.5 0 0 1 1.5 2a1 1 0 0 1 1-1z" fill="var(--gold)"/></svg>
      972-555-0148
    </li>
    <li>
      <svg viewBox="0 0 12 12" aria-hidden="true"><rect x="0.8" y="2.3" width="10.4" height="7.4" fill="none" stroke="var(--gold)" stroke-width="1.2"/><path d="M1 2.6 6 6.6l5-4" fill="none" stroke="var(--gold)" stroke-width="1.2"/></svg>
      info@tovrel-woundcare.com
    </li>
    <li>
      <svg viewBox="0 0 12 12" aria-hidden="true"><circle cx="6" cy="6" r="5" fill="var(--gold)"/><path d="M1 6h10M6 1v10M6 1c-2.6 2.8-2.6 7.2 0 10M6 1c2.6 2.8 2.6 7.2 0 10" fill="none" stroke="var(--card)" stroke-width="0.8"/></svg>
      www.tovrel-woundcare.com
    </li>
  </ul>

  <p class="address">2180 Harlow Ave Ste 200, PMB 114806 Dallas, TX 75219</p>
</section>

<section class="card card--back" aria-label="Business card back">
  <div class="pattern" role="img" aria-label="Embossed repeating brand monogram pattern in dark charcoal tones"></div>
  <p class="back-name">TOVREL</p>
</section>

</body>
</html>
```